We need an attractive business card design that is modern and inviting. We like the blue and yellow (or gold) colors that are displayed with the logo. The business should communicate trust, experience, and integrity.

Target Market(s)

Residential and Commercial

Industry/Entity Type

Business

Contact Information for Business Card

Recessed Lighting
LED Retro Fit
Sign Repair
Alarms and Cameras
Mobile Home Services
24hr service calls

Font styles to use
Serif
Sans Serif

Colors
3176b5
0455a3
fece3e
fbee3e

Requirements
Must have
• Brondle Electric
• Owner: Marcus Tivane
• Licensed and Insured
• TECL #58917
Nice to have
• Exquisite Detail!!
• Over 20 years of experience
Should not have
• Nothing boring or traditional!!!

```html
<!DOCTYPE html>
<html lang="en">
<head>
<meta charset="utf-8">
<title>Brondle Electric – Business Card</title>
<link href="https://fonts.googleapis.com/css2?family=Fira+Sans:wght@400;600;700;800&display=swap" rel="stylesheet">
<style>
  :root {
    --navy: #0a2b5c;
    --navy-glow: #1d4679;
    --brand-blue: #0455a3;
    --brand-blue-soft: #3176b5;
    --brand-yellow: #fbee3e;
    --brand-gold: #fece3e;
    --icon-grey: #8d97a5;
    --text-white: #ffffff;
    --page: #ffffff;
  }
  * { box-sizing: border-box; margin: 0; padding: 0; }
  html, body {
    width: 1200px; height: 1200px; overflow: hidden;
    background: var(--page);
    font-family: "Fira Sans", Arial, sans-serif;
  }
  .sheet {
    width: 1200px; height: 1200px;
    display: flex; flex-direction: column; align-items: center; justify-content: center;
    gap: 60px;
  }
  .card {
    position: relative;
    width: 880px; height: 500px;
    border-radius: 16px;
    overflow: hidden;
    background: radial-gradient(ellipse at 55% 65%, var(--navy-glow) 0%, var(--navy) 60%);
    color: var(--text-white);
  }
  .card__edge {
    position: absolute; left: 0; right: 0; bottom: 0; height: 16px;
    background: var(--brand-yellow);
  }

  /* Back: contact side */
  .contact {
    display: flex; align-items: center; height: 100%; padding: 0 70px 16px;
  }
  .contact__mark {
    width: 270px; height: 270px; border-radius: 50%;
    border: 22px solid var(--brand-blue); flex-shrink: 0;
  }
  .contact__divider {
    width: 3px; height: 250px; background: var(--text-white);
    margin: 0 50px 0 70px; opacity: .9;
  }
  .contact__name { font-size: 40px; font-weight: 700; letter-spacing: 1px; }
  .contact__role {
    font-size: 22px; font-weight: 700; color: var(--brand-yellow);
    letter-spacing: 1.5px; margin-top: 4px;
  }
  .contact__lines { list-style: none; margin-top: 34px; }
  .contact__line {
    display: flex; align-items: center; gap: 14px;
    font-size: 26px; font-weight: 400; margin-bottom: 14px;
  }
  .contact__line svg { width: 26px; height: 26px; }

  /* Front: services side */
  .brand {
    display: flex; align-items: center; gap: 44px;
    padding: 58px 0 0 110px;
  }
  .brand__circle {
    width: 130px; height: 130px; border-radius: 50%;
    border: 14px solid var(--brand-blue);
  }
  .brand__name {
    font-size: 62px; font-weight: 800; letter-spacing: 1px;
    color: var(--brand-yellow);
  }
  .services {
    list-style: none;
    display: grid; grid-template-columns: 450px 1fr;
    grid-auto-flow: column; grid-template-rows: repeat(4, 62px);
    padding: 52px 0 0 90px;
  }
  .service {
    display: flex; align-items: center; gap: 22px;
    font-size: 28px; font-weight: 600;
  }
  .service__icon {
    width: 50px; height: 50px; border-radius: 50%;
    background: var(--icon-grey); flex-shrink: 0;
    display: flex; align-items: center; justify-content: center;
  }
  .service__icon svg { width: 30px; height: 30px; }
</style>
</head>
<body>
<main class="sheet">

  <section class="card card--back" aria-label="Card back, contact details">
    <div class="contact">
      <div class="contact__mark" aria-hidden="true"></div>
      <div class="contact__divider"></div>
      <div class="contact__info">
        <p class="contact__name">Marcus Tivane</p>
        <p class="contact__role">Owner</p>
        <ul class="contact__lines">
          <li class="contact__line">
            <svg viewBox="0 0 24 24" fill="none" stroke="#fff" stroke-width="2"><rect x="6" y="2" width="12" height="20" rx="2"/><line x1="10" y1="18" x2="14" y2="18"/></svg>
            (000) 000-0000
          </li>
          <li class="contact__line">
            <svg viewBox="0 0 24 24" fill="none" stroke="#fff" stroke-width="2"><path d="M5 4h4l2 5-3 2a11 11 0 0 0 5 5l2-3 5 2v4a2 2 0 0 1-2 2A17 17 0 0 1 3 6a2 2 0 0 1 2-2z"/></svg>
            (000) 000-0000
          </li>
        </ul>
      </div>
    </div>
    <div class="card__edge"></div>
  </section>

  <section class="card card--front" aria-label="Card front, services">
    <header class="brand">
      <div class="brand__circle" aria-hidden="true"></div>
      <h1 class="brand__name">BRONDLE ELECTRIC</h1>
    </header>
    <ul class="services">
      <li class="service">
        <span class="service__icon"><svg viewBox="0 0 24 24" fill="none" stroke="#fff" stroke-width="2"><rect x="3" y="8" width="8" height="13"/><rect x="11" y="3" width="10" height="18"/><path d="M6 12h2M6 16h2M14 7h4M14 11h4M14 15h4"/></svg></span>
        Residential and Commercial
      </li>
      <li class="service">
        <span class="service__icon"><svg viewBox="0 0 24 24" fill="none" stroke="#fff" stroke-width="2"><circle cx="12" cy="12" r="5"/><path d="M12 1v3M12 20v3M1 12h3M20 12h3M4.2 4.2l2 2M17.8 17.8l2 2M4.2 19.8l2-2M17.8 6.2l2-2"/></svg></span>
        Recessed Lighting
      </li>
      <li class="service">
        <span class="service__icon"><svg viewBox="0 0 24 24" fill="none" stroke="#fff" stroke-width="2"><circle cx="12" cy="12" r="5"/><path d="M12 1v3M12 20v3M1 12h3M20 12h3M4.2 4.2l2 2M17.8 17.8l2 2M4.2 19.8l2-2M17.8 6.2l2-2"/></svg></span>
        LED Retro Fit
      </li>
      <li class="service">
        <span class="service__icon"><svg viewBox="0 0 24 24" fill="none" stroke="#fff" stroke-width="2"><circle cx="9" cy="9" r="3"/><circle cx="16.5" cy="16.5" r="2.5"/><path d="M9 3v2M9 13v2M3 9h2M13 9h2M16.5 11.5v1.5M16.5 20v1.5M11.5 16.5h1.5M20 16.5h1.5"/></svg></span>
        Sign Repair
      </li>
      <li class="service">
        <span class="service__icon"><svg viewBox="0 0 24 24" fill="none" stroke="#fff" stroke-width="2"><rect x="3" y="6" width="14" height="8" rx="1" transform="rotate(15 10 10)"/><path d="M9 15l-2 6M4 21h6"/><circle cx="18" cy="11" r="1"/></svg></span>
        Alarms and Cameras
      </li>
      <li class="service">
        <span class="service__icon"><svg viewBox="0 0 24 24" fill="none" stroke="#fff" stroke-width="2"><rect x="4" y="6" width="9" height="15" rx="1.5"/><rect x="13" y="3" width="7" height="12" rx="1.5"/></svg></span>
        Mobile Home Services
      </li>
      <li class="service">
        <span class="service__icon"><svg viewBox="0 0 24 24" fill="none" stroke="#fff" stroke-width="2"><path d="M20 12a8 8 0 1 1-3-6.2"/><path d="M17 2v4h4"/><text x="12" y="15" font-size="8" font-family="Fira Sans, sans-serif" font-weight="700" fill="#fff" stroke="none" text-anchor="middle">24</text></svg></span>
        24hr service calls
      </li>
    </ul>
    <div class="card__edge"></div>
  </section>

</main>
</body>
</html>
```